Roof Plumbing Company needs simple, modern business card using the attached logo and below details:

Dean Halloway
Summit Gutters Pty Ltd
ABN: 58 214 937 062
Phone: 0417 286 531
Email: summitgutters@mailbrook.com
Website: summitgutters.com.au

For all of your metal roof plumbing requirements contact Summit Gutters for an obligation free quote - no job too big or to small!

Industry/Entity Type

Business

Contact Information for Business Card

Dean Halloway
Summit Gutters Pty Ltd
ABN 58 214 937 062
0417 286 531
summitgutters@mailbrook.com
summitgutters.com.au

Requirements
Must have
• Bright eye catching design, professional look

```html
<!DOCTYPE html>
<html lang="en">
<head>
<meta charset="utf-8">
<title>Summit Gutters – Business Card</title>
<link rel="stylesheet" href="https://fonts.googleapis.com/css2?family=Montserrat:wght@700&family=Mulish:wght@400;500&display=swap">
<style>
  :root {
    --page-bg: #e6e6e6;
    --card-bg: #f7f7f6;
    --card-edge: #cfcfcf;
    --brand-red: #8e1a1d;
    --band-red: #961c1f;
    --ink: #1f1f1f;
    --band-text: #f4e9e9;
  }
  * { margin: 0; padding: 0; box-sizing: border-box; }
  html, body {
    width: 1200px;
    height: 970px;
    overflow: hidden;
    background: var(--page-bg);
  }
  .card {
    position: absolute;
    left: 100px;
    top: 207px;
    width: 1000px;
    height: 556px;
    background: var(--card-bg);
    border: 1px solid var(--card-edge);
  }
  .brand {
    position: absolute;
    left: 60px;
    top: 170px;
    width: 440px;
    display: flex;
    align-items: center;
    gap: 18px;
  }
  .brand-mark {
    flex: none;
    width: 34px;
    height: 34px;
    background: var(--brand-red);
  }
  .brand-name {
    font-family: "Montserrat", sans-serif;
    font-weight: 700;
    font-size: 44px;
    line-height: 1.08;
    color: var(--brand-red);
    text-transform: uppercase;
    letter-spacing: 1px;
  }
  .contact {
    position: absolute;
    left: 574px;
    top: 112px;
  }
  .contact-name {
    font-family: "Montserrat", sans-serif;
    font-weight: 700;
    font-size: 32px;
    color: var(--brand-red);
    letter-spacing: 0.5px;
    margin-bottom: 46px;
  }
  .contact-list { list-style: none; }
  .contact-item {
    font-family: "Mulish", sans-serif;
    font-weight: 500;
    font-size: 24px;
    color: var(--ink);
    height: 36px;
    display: flex;
    align-items: center;
    gap: 10px;
  }
  .contact-item.abn { margin-bottom: 6px; }
  .contact-icon { width: 22px; height: 22px; flex: none; }
  .tagline {
    position: absolute;
    left: 0;
    top: 435px;
    width: 100%;
    height: 88px;
    background: var(--band-red);
    display: flex;
    align-items: center;
    justify-content: center;
    text-align: center;
    font-family: "Mulish", sans-serif;
    font-weight: 400;
    font-size: 23px;
    line-height: 1.4;
    color: var(--band-text);
  }
</style>
</head>
<body>
  <section class="card">
    <div class="brand">
      <span class="brand-mark"></span>
      <span class="brand-name">Summit Gutters<br>Pty Ltd</span>
    </div>

    <div class="contact">
      <h1 class="contact-name">DEAN HALLOWAY</h1>
      <ul class="contact-list">
        <li class="contact-item abn">ABN 58 214 937 062</li>
        <li class="contact-item">
          <svg class="contact-icon" viewBox="0 0 24 24" aria-hidden="true"><path fill="#8e1a1d" d="M6.6 10.8a15.1 15.1 0 0 0 6.6 6.6l2.2-2.2a1 1 0 0 1 1-.25 11.4 11.4 0 0 0 3.6.57 1 1 0 0 1 1 1V20a1 1 0 0 1-1 1A17 17 0 0 1 3 4a1 1 0 0 1 1-1h3.5a1 1 0 0 1 1 1c0 1.25.2 2.45.57 3.6a1 1 0 0 1-.25 1z"/></svg>
          0417 286 531
        </li>
        <li class="contact-item">
          <svg class="contact-icon" viewBox="0 0 24 24" aria-hidden="true"><rect x="2" y="5" width="20" height="14" fill="#8e1a1d"/><path d="M2.5 5.5 12 13l9.5-7.5" fill="none" stroke="#f7f7f6" stroke-width="1.6"/></svg>
          summitgutters@mailbrook.com
        </li>
        <li class="contact-item">
          <svg class="contact-icon" viewBox="0 0 24 24" aria-hidden="true"><circle cx="12" cy="12" r="9.5" fill="none" stroke="#8e1a1d" stroke-width="2"/><path d="M2.5 12h19M12 2.5c3 3 3 16 0 19M12 2.5c-3 3-3 16 0 19" fill="none" stroke="#8e1a1d" stroke-width="1.6"/></svg>
          summitgutters.com.au
        </li>
      </ul>
    </div>

    <p class="tagline">For all of your metal roof plumbing requirements contact Summit Gutters for<br>an obligation free quote - no job too big or to small!</p>
  </section>
</body>
</html>
```